We need a business card design for a Dubai based company .

We need a business card for a Dubai based company called "Zernova Smoking Requisites Trading LLC". We mainly import Flavoured Tobacco products and Charcoal which is used for smoking in a Hookah/Shisha and distribute to the wholesalers and retailers. Logo file is attached herewith.

```html
<!DOCTYPE html>
<html lang="en">
<head>
<meta charset="utf-8">
<title>Zernova Smoking Requisites Trading LLC – Business Card</title>
<link rel="stylesheet" href="https://fonts.googleapis.com/css2?family=Michroma&family=Exo+2:wght@400;500&display=swap">
<style>
  :root {
    --bg: #e4e4e4;
    --brand-red: #c6343b;
    --brand-red-light: #cf4a50;
    --brand-red-deep: #b2272e;
    --art-tone-a: #b8323a;
    --art-tone-b: #a82a31;
    --paper: #fbfbfb;
    --ink: #3a3a3d;
    --white: #ffffff;
  }
  * { box-sizing: border-box; margin: 0; padding: 0; }
  html, body {
    width: 1200px; height: 800px; overflow: hidden;
    background: var(--bg);
  }
  .canvas {
    position: relative; width: 1200px; height: 800px;
    display: flex; align-items: center; justify-content: center; gap: 60px;
  }
  .card {
    position: relative; width: 500px; height: 300px;
    box-shadow: 0 10px 24px rgba(0,0,0,0.14);
  }

  /* Front */
  .card-front {
    background: linear-gradient(135deg, var(--brand-red-light), var(--brand-red) 55%, var(--brand-red-deep));
    display: flex; align-items: center; justify-content: center;
  }
  .art-area {
    position: absolute; left: 180px; top: 60px; width: 140px; height: 160px;
    background: linear-gradient(180deg, var(--art-tone-a), var(--art-tone-b));
  }
  .wordmark {
    position: relative; text-align: center;
    font-family: "Michroma", sans-serif; font-weight: 400;
    color: var(--white);
  }
  .card-front .wordmark-name { display: block; font-size: 28px; letter-spacing: 3px; }
  .card-front .wordmark-tag { display: block; font-size: 7px; letter-spacing: 2.4px; margin-top: 8px; }

  /* Back */
  .card-back {
    background: var(--brand-red);
    padding: 18px;
  }
  .card-back-inner {
    position: relative; width: 100%; height: 100%;
    background: var(--paper);
  }
  .holder-name {
    position: absolute; left: 34px; top: 34px;
    font-family: "Michroma", sans-serif; font-weight: 400; font-size: 21px; letter-spacing: 1px;
    color: var(--ink);
  }
  .holder-role {
    position: absolute; left: 36px; top: 66px;
    font-family: "Exo 2", sans-serif; font-size: 12px; letter-spacing: 4px;
    color: var(--brand-red);
  }
  .back-wordmark {
    position: absolute; left: 34px; top: 150px;
    font-family: "Michroma", sans-serif; font-weight: 400; color: var(--ink);
  }
  .back-wordmark .wordmark-name { display: block; font-size: 16px; letter-spacing: 1.5px; }
  .back-wordmark .wordmark-tag { display: block; font-size: 4.5px; letter-spacing: 1.2px; margin-top: 4px; }
  .contact {
    position: absolute; left: 250px; top: 170px;
    font-family: "Exo 2", sans-serif; font-size: 13px; line-height: 20px;
    color: var(--ink); list-style: none;
  }
  .contact-label { color: var(--brand-red); display: inline-block; width: 16px; }
  .contact-address { margin-top: 2px; line-height: 17px; }
</style>
</head>
<body>
<main class="canvas">
  <section class="card card-front" aria-label="Card front">
    <div class="art-area" role="img" aria-label="Dark red watercolour artwork behind the company name"></div>
    <div class="wordmark">
      <span class="wordmark-name">ZERNOVA</span>
      <span class="wordmark-tag">SMOKING REQUISITES TRADING LLC</span>
    </div>
  </section>

  <section class="card card-back" aria-label="Card back">
    <div class="card-back-inner">
      <h1 class="holder-name">MARCO DELANEY</h1>
      <p class="holder-role">OWNER | MANAGER</p>
      <div class="back-wordmark">
        <span class="wordmark-name">ZERNOVA</span>
        <span class="wordmark-tag">SMOKING REQUISITES TRADING LLC</span>
      </div>
      <ul class="contact">
        <li><span class="contact-label">P</span>0412 555 017</li>
        <li><span class="contact-label">E</span>info@zernovallc.com</li>
        <li class="contact-address">Glenmoor, Sydney,<br>NSW, 2199</li>
      </ul>
    </div>
  </section>
</main>
</body>
</html>
```